Very Simple/Minimal Business Card Design Project

The company operates in the industrial maritime infrastructure sector in Brazil. You can find more information on our website www.navelquor.com.br WE NEED TO LOOK POWERFUL AND SERIOUS
I have attached a copy of the old cards. We would like something more professional / industrial / sexy that also includes the position.

The card can be double sided or not. We would like you to propose as many options.

Thank you
Updates

Many thanks, do let me know if you have any questions. I am under a lot of time pressure to try and have them printed over the next days or so.

Please could you use the following information

for the address: Rua Tapiraçu, 418 - Centro, Rio de Janeiro, 20135-070, Brasil

for the mobile: +55 21 8372 9041
for the landline: +55 21 4067 3859

and position:  Diretor Geral

Thakn you

Target Market(s)

Shipowners, bankers, industrial companies

Industry/Entity Type

Industrial

Requirements
Must have
• POWERFUL
SERIOUS
SOLID
BIG CORPORATION

```html
<!DOCTYPE html>
<html lang="pt-BR">
<head>
<meta charset="utf-8">
<title>Navelquor – Cartão de Visita</title>
<link rel="stylesheet" href="https://fonts.googleapis.com/css2?family=Encode+Sans+Semi+Condensed:wght@400;800&display=swap">
<style>
  :root {
    --page-bg: #ffffff;
    --card-bg: #ffffff;
    --card-border: #6d6d6d;
    --navy: #10297a;
    --ink-navy: #1a2a6c;
    --brand-green: #0f9a3e;
    --wave-green: #16a84c;
    --wave-blue: #0b3f8d;
    --on-dark: #ffffff;
  }
  * { box-sizing: border-box; }
  html, body {
    margin: 0;
    width: 1200px;
    height: 1000px;
    overflow: hidden;
    background: var(--page-bg);
    font-family: "Encode Sans Semi Condensed", "Arial Narrow", sans-serif;
  }
  .business-card {
    position: absolute;
    left: 75px;
    top: 200px;
    width: 1050px;
    height: 600px;
    background: var(--card-bg);
    border: 1px solid var(--card-border);
    overflow: hidden;
  }
  .card-waves {
    position: absolute;
    inset: 0;
    width: 100%;
    height: 100%;
  }
  .email {
    position: absolute;
    right: 24px;
    top: 24px;
    margin: 0;
    font-size: 31px;
    font-weight: 400;
    color: var(--brand-green);
  }
  .brand {
    position: absolute;
    left: 25px;
    top: 62px;
    display: flex;
    align-items: center;
    gap: 18px;
  }
  .brand-square {
    width: 120px;
    height: 120px;
    border-radius: 9px;
    background: var(--brand-green);
  }
  .brand-name {
    margin: 0;
    font-size: 82px;
    font-weight: 800;
    line-height: 1;
    color: var(--navy);
    letter-spacing: 1px;
  }
  .holder {
    position: absolute;
    left: 0;
    right: 0;
    top: 246px;
    text-align: center;
    color: var(--ink-navy);
  }
  .holder-name {
    margin: 0;
    font-size: 37px;
    font-weight: 400;
    line-height: 48px;
    letter-spacing: 7px;
  }
  .holder-role {
    margin: 4px 0 0;
    font-size: 22px;
    font-weight: 400;
    line-height: 28px;
    letter-spacing: 5px;
    text-transform: uppercase;
    color: var(--brand-green);
  }
  .phones, .address {
    position: absolute;
    margin: 0;
    font-style: normal;
    font-size: 32px;
    font-weight: 400;
    line-height: 45px;
    color: var(--on-dark);
  }
  .phones { left: 25px; bottom: 14px; }
  .address { right: 24px; bottom: 14px; text-align: right; }
  .phones span, .address span { display: block; }
</style>
</head>
<body>
  <article class="business-card">
    <svg class="card-waves" viewBox="0 0 1050 600" preserveAspectRatio="none" aria-hidden="true">
      <path fill="var(--wave-green)" d="M0,345 C200,398 350,418 480,410 C700,396 850,300 1050,300 L1050,600 L0,600 Z"/>
      <path fill="var(--wave-blue)" d="M0,345 C200,410 360,435 500,432 C720,428 880,358 1050,358 L1050,600 L0,600 Z"/>
    </svg>

    <p class="email">rafael@navelquor.com.br</p>

    <div class="brand">
      <div class="brand-square"></div>
      <h1 class="brand-name">NAVELQUOR</h1>
    </div>

    <div class="holder">
      <h2 class="holder-name">Rafael Montenegro</h2>
      <p class="holder-role">Diretor Geral</p>
    </div>

    <p class="phones">
      <span>T: + 55 21 4067 3859</span>
      <span>M: + 55 21 8372 9041</span>
    </p>

    <address class="address">
      <span>R. Tapiraçu 418</span>
      <span>Centro</span>
      <span>CEP 20135-070</span>
      <span>Rio de Janeiro</span>
    </address>
  </article>
</body>
</html>
```